Ridgeline Stick Works
Custom Wood Bats
guaranteed please...
For some reason, my numbers aren't showing up, but for the ones I rated, could you put the rest of the stationary with the cards? Looks great you all. Thanks!
increase the price please.....
#3, I like that. Can you make the seams red on the front of the ball or will the address not show up if you do?
Can you combine 7 & 8
Hi - so it is ok to alter the logo colors on the logo itself?
I would like to see some different colors. Maybe a navy blue print on the logo and then in the red part. Leave the ball white with red stitches. Look forward to seeing your interpretations.
Just uploaded it. My name doesn't have a "c" in it. Could you also put "Ridgeline Stick Works" somewhere on the front of the card? Also, I'm not a big fan of the all caps. Thanks for your design.
can you upload the original logo,please?

```html
<!DOCTYPE html>
<html lang="en">
<head>
<meta charset="utf-8">
<title>Ridgeline Stick Works — Stationery Set</title>
<link href="https://fonts.googleapis.com/css2?family=Tinos:wght@400;700&display=swap" rel="stylesheet">
<style>
  :root {
    --navy: #0d3f8f;
    --blue: #1d5fc2;
    --blue-light: #4f8fe0;
    --red: #c8202e;
    --paper: #ffffff;
    --ink: #1d4f9a;
    --edge: #d9dde3;
  }
  * { box-sizing: border-box; margin: 0; padding: 0; }
  html, body { width: 1200px; height: 744px; overflow: hidden; background: var(--paper); }
  body { position: relative; font-family: "Tinos", "Times New Roman", serif; color: var(--ink); }

  .sheet { position: absolute; background: var(--paper); border: 1px solid var(--edge); overflow: hidden; }

  .wordmark { display: flex; align-items: center; gap: 6px; font-weight: 700; color: var(--navy); white-space: nowrap; }
  .wordmark .dot { border-radius: 50%; background: var(--red); flex: none; }
  .wordmark.on-blue { color: var(--paper); }

  /* Letterhead */
  .letterhead { left: 53px; top: 24px; width: 523px; height: 696px; }
  .letterhead .band-top { position: absolute; left: 0; top: 0; width: 100%; height: 8px; background: linear-gradient(90deg, var(--navy), var(--blue-light) 50%, var(--navy)); }
  .letterhead .band-bottom { position: absolute; left: 0; bottom: 0; width: 100%; height: 10px; background: linear-gradient(90deg, var(--navy), var(--blue-light) 50%, var(--navy)); }
  .letterhead .wordmark { position: absolute; left: 10px; top: 30px; font-size: 19px; }
  .letterhead .wordmark .dot { width: 14px; height: 14px; }
  .letterhead .contact { position: absolute; left: 10px; bottom: 22px; font-size: 11px; line-height: 14px; }

  /* Business card front */
  .card-front { left: 600px; top: 36px; width: 192px; height: 120px; }
  .card-front .band { position: absolute; left: 0; top: 0; width: 100%; height: 4px; background: var(--blue); }
  .card-front .wordmark { position: absolute; left: 8px; top: 14px; font-size: 10px; gap: 4px; }
  .card-front .wordmark .dot { width: 8px; height: 8px; }
  .card-front .person { position: absolute; left: 14px; top: 60px; font-size: 9px; line-height: 11px; }
  .card-front .person .role { font-size: 6px; color: #6a7a95; }
  .card-front .details { position: absolute; left: 110px; top: 52px; font-size: 5.5px; line-height: 7px; }

  /* Card backs */
  .card-back { position: absolute; display: flex; align-items: center; justify-content: center;
    background: radial-gradient(ellipse at center, var(--blue-light) 0%, var(--blue) 45%, var(--navy) 100%); }
  .card-back.one { left: 679px; top: 283px; width: 156px; height: 101px; }
  .card-back.two { left: 931px; top: 302px; width: 154px; height: 96px; }
  .card-back .wordmark { font-size: 11px; gap: 4px; }
  .card-back .wordmark .dot { width: 8px; height: 8px; }

  /* Envelope */
  .envelope { left: 581px; top: 499px; width: 511px; height: 221px; }
  .envelope .flap { position: absolute; left: 0; top: 0; width: 100%; height: 88px;
    background: radial-gradient(ellipse at 50% 55%, var(--blue-light) 0%, var(--blue) 40%, var(--navy) 100%); }
  .envelope .flap .wordmark { position: absolute; left: 50%; top: 34px; transform: translateX(-50%) rotate(180deg); font-size: 17px; }
  .envelope .flap .wordmark .dot { width: 12px; height: 12px; }
  .envelope .return-mark { position: absolute; left: 12px; top: 122px; font-size: 18px; }
  .envelope .return-mark .dot { width: 13px; height: 13px; }
  .envelope .return-address { position: absolute; left: 12px; top: 176px; font-size: 9px; }
  .envelope .band-bottom { position: absolute; left: 0; bottom: 0; width: 100%; height: 7px; background: linear-gradient(90deg, var(--navy), var(--blue-light) 50%, var(--navy)); }
</style>
</head>
<body>

  <section class="sheet letterhead" aria-label="Letterhead">
    <div class="band-top"></div>
    <div class="wordmark"><span class="dot"></span>Ridgeline Stick Works</div>
    <address class="contact" style="font-style:normal">
      PO Box 412 · Alder Falls, NC 28140<br>
      Phone: 704.555.0182<br>
      Email: dana.holt@ridgelinestick.com<br>
      www.ridgelinestick.com
    </address>
    <div class="band-bottom"></div>
  </section>

  <section class="sheet card-front" aria-label="Business card front">
    <div class="band"></div>
    <div class="wordmark"><span class="dot"></span>Ridgeline Stick Works</div>
    <div class="person">Dana Holt<br><span class="role">Owner</span></div>
    <div class="details">
      PO Box 412<br>
      Alder Falls, NC 28140<br>
      Phone: 704.555.0182<br>
      Cell: 704.555.0147<br>
      Email: dana.holt@ridgelinestick.com<br>
      www.ridgelinestick.com
    </div>
  </section>

  <section class="card-back one" aria-label="Business card back">
    <div class="wordmark on-blue"><span class="dot"></span>Ridgeline Stick Works</div>
  </section>

  <section class="card-back two" aria-label="Business card back, alternate">
    <div class="wordmark on-blue"><span class="dot"></span>Ridgeline Stick Works</div>
  </section>

  <section class="sheet envelope" aria-label="Envelope">
    <div class="flap">
      <div class="wordmark on-blue"><span class="dot"></span>Ridgeline Stick Works</div>
    </div>
    <div class="wordmark return-mark"><span class="dot"></span>Ridgeline Stick Works</div>
    <div class="return-address">PO Box 412, Alder Falls, NC 28140</div>
    <div class="band-bottom"></div>
  </section>

</body>
</html>
```